Business card for law firm

Need business card for new law firm. Think confident, authoritative, conservative, but not stuffy or old-fashioned.

Contact Information for Business Card

Content for card - logo (uploaded), plus the following:

Paul Wexbury (larger font)
Managing Partner (larger font, but not as large as name)
Level 9, 41 Tansy Lane
Sydney NSW 2000
Main Tel 02 7346 2190
Direct Tel 02 6273 4415
Email paul@qvlegal.com.au
www.qvlegal.com.au

Letterhead design should include logo plus:
Level 9, 41 Tansy Lane
Sydney NSW 2000
Tel 02 6273 4415
www.qvlegal.com.au

```html
<!DOCTYPE html>
<html lang="en">
<head>
<meta charset="utf-8">
<title>Quillvane Legal — Business Card</title>
<link rel="stylesheet" href="https://fonts.googleapis.com/css2?family=EB+Garamond:wght@400&family=Open+Sans:wght@400&display=swap">
<style>
  :root {
    --navy: #1d2357;
    --ink: #141414;
    --text: #2a2a2a;
    --paper: #ffffff;
    --backdrop: #e6e1d9;
    --tint: #e9eaf0;
  }
  * { margin: 0; padding: 0; box-sizing: border-box; }
  html, body { width: 1200px; height: 1200px; overflow: hidden; }
  body { background: var(--backdrop); position: relative; }

  .card {
    position: absolute;
    left: 75px; top: 313px;
    width: 1050px; height: 573px;
    background: var(--paper);
    overflow: hidden;
    box-shadow: 0 6px 18px rgba(0,0,0,0.12);
  }

  .brand-mark {
    position: absolute;
    left: 72px; top: 47px;
    width: 134px; height: 134px;
    background: var(--navy);
  }
  .brand-name {
    position: absolute;
    left: 258px; top: 78px;
    font-family: "EB Garamond", serif;
    font-weight: 400;
    color: var(--ink);
    line-height: 1;
  }
  .brand-name .primary { display: block; font-size: 70px; letter-spacing: 1px; }
  .brand-name .secondary { display: block; font-size: 36px; letter-spacing: 29px; margin-top: 2px; }
  .brand-rule {
    position: absolute;
    left: 258px; top: 197px;
    width: 674px; height: 3px;
    background: var(--navy);
  }

  .contact {
    position: absolute;
    left: 68px; top: 312px;
    list-style: none;
    font-family: "Open Sans", sans-serif;
    font-size: 26px;
    color: var(--text);
    line-height: 32px;
  }
  .contact li { display: flex; align-items: center; margin-bottom: 10px; }
  .contact li.single { margin-bottom: 11px; }
  .contact .icon { width: 36px; height: 36px; margin-right: 28px; flex: none; }
  .contact .icon svg { width: 36px; height: 36px; display: block; }

  .backdrop-tint {
    position: absolute;
    left: 666px; top: 317px;
    width: 253px; height: 256px;
    background: var(--tint);
  }

  .person {
    position: absolute;
    right: 86px; top: 418px;
    text-align: right;
  }
  .person .name {
    font-family: "EB Garamond", serif;
    font-size: 56px;
    color: var(--ink);
    line-height: 1;
  }
  .person .role {
    font-family: "Open Sans", sans-serif;
    font-size: 30px;
    color: var(--navy);
    line-height: 1.1;
    margin-top: 2px;
  }
</style>
</head>
<body>
  <div class="card">
    <div class="brand-mark"></div>
    <div class="brand-name">
      <span class="primary">QUILLVANE</span>
      <span class="secondary">LEGAL</span>
    </div>
    <div class="brand-rule"></div>

    <div class="backdrop-tint"></div>

    <ul class="contact">
      <li>
        <span class="icon"><svg viewBox="0 0 36 36"><path fill="var(--navy)" d="M18 3a11 11 0 0 0-11 11c0 8 11 19 11 19s11-11 11-19A11 11 0 0 0 18 3zm0 15.5a4.5 4.5 0 1 1 0-9 4.5 4.5 0 0 1 0 9z"/></svg></span>
        <span>Level 9, 41 Tansy Lane<br>Sydney NSW 2000</span>
      </li>
      <li>
        <span class="icon"><svg viewBox="0 0 36 36"><path fill="var(--navy)" d="M11 5l5 7-3 3c1 4 4 7 8 9l3-3 7 5-3 4c-12-1-20-10-21-21z"/></svg></span>
        <span>Main: 02 7346 2190<br>Direct: 02 6273 4415</span>
      </li>
      <li class="single">
        <span class="icon"><svg viewBox="0 0 36 36"><rect x="2" y="9" width="32" height="20" fill="var(--navy)"/><path d="M3 10l15 11 15-11" fill="none" stroke="#fff" stroke-width="2.2"/></svg></span>
        <span>paul@qvlegal.com.au</span>
      </li>
      <li class="single">
        <span class="icon"><svg viewBox="0 0 36 36"><g fill="none" stroke="var(--navy)" stroke-width="2.4"><circle cx="18" cy="18" r="13"/><ellipse cx="18" cy="18" rx="6" ry="13"/><path d="M5 18h26M7 11h22M7 25h22M18 5v26"/></g></svg></span>
        <span>www.qvlegal.com.au</span>
      </li>
    </ul>

    <div class="person">
      <div class="name">Paul Wexbury</div>
      <div class="role">Managing Partner</div>
    </div>
  </div>
</body>
</html>
```